Re-brand our business and design!

We need a simple informational website (editable for in the future use)
We need our logo(we have included logo), name, who we are, and what we do displayed.

This is our current site (which is not acceptable, and only a template site): all our information is on this site, please use it forreferanceofinformation.
Www.brightlanefixers.com

Target Market(s)

Real estate brokers, and realtors,homeowners, and anyone looking for home repairs.

Industry/Entity Type

Business

Number of Pages Required

4 page

Font styles to use
Sans Serif

Requirements
Must have
• Our name, contact info, services, and our logo (which we will Email upon request)
• MUST have originality to the site.
• custom "contact us form" or request an estimate form.
Nice to have
• page for real customer testimonies.
• page for our previous work where we can upload pics of completed jobs.
Should not have
• any infringements on any copyrights or plagiarism at all.

```html
<!DOCTYPE html>
<html lang="en">
<head>
<meta charset="utf-8">
<title>Bright Lane Fixers – Home Repairs and Maintenance</title>
<link href="https://fonts.googleapis.com/css2?family=Lato:wght@400;700;900&family=Roboto:wght@300;400&family=Roboto+Condensed:wght@400;700&family=Montserrat:wght@400;500&display=swap" rel="stylesheet">
<style>
:root{
  --red:#e31e24;
  --ink:#1a1a1a;
  --grey:#666;
  --muted:#8a8a8a;
  --band:#a5a6a8;
  --stage:#ececec;
  --white:#fff;
}
*{box-sizing:border-box;margin:0;padding:0}
html,body{width:1200px;height:1200px;overflow:hidden;background:var(--stage);font-family:"Lato",sans-serif}
.page{position:absolute;left:191px;top:53px;width:820px;height:1094px;background:var(--white);box-shadow:0 6px 30px rgba(0,0,0,.25);overflow:hidden}
.abs{position:absolute}

/* top bar */
.topbar{left:0;top:0;width:820px;height:36px;background:var(--red);color:var(--white);font-size:10px;font-family:"Montserrat",sans-serif}
.topbar .call{left:31px;top:13px}
.social{display:flex;gap:10px}
.topbar .social{left:607px;top:12px}
.social span{width:12px;height:12px;border-radius:50%;border:1.5px solid var(--white);display:block}
.topbar .search{left:731px;top:11px;display:flex;align-items:center;gap:8px}

/* brand */
.brand{left:0;top:118px;width:820px;text-align:center}
.brand-name{font-weight:900;font-size:22px;color:var(--ink);display:inline-flex;align-items:center;gap:10px}
.brand-name i{width:14px;height:14px;background:var(--red);display:block}
.brand-sub{font-weight:700;font-size:15px;color:#555;margin-top:4px;letter-spacing:.3px}

/* nav */
.nav{top:183px;font-family:"Montserrat",sans-serif;font-size:13px;color:#444;font-weight:500}
.nav.active{color:var(--red)}

/* hero */
.hero{left:0;top:215px;width:820px;height:327px;background:linear-gradient(160deg,#6f8a4f 0%,#9aa7a3 30%,#8b7f76 55%,#a67f6a 75%,#5f5a52 100%)}
.hero-overlay{left:0;top:233px;width:820px;height:94px;background:rgba(40,35,30,.55);color:var(--white);text-align:center;z-index:1}
.hero-overlay p{font-size:13px;line-height:16px}
.hero-overlay p:first-child{margin-top:12px}
.hero-overlay h1{font-family:"Roboto Condensed",sans-serif;font-weight:400;font-size:28px;margin-top:10px;letter-spacing:.3px}

.quote-form{left:609px;top:36px;width:157px;z-index:2}
.field{background:var(--white);border-radius:2px;height:22px;margin-bottom:7px;font-size:9px;color:#999;padding:5px 6px;font-family:"Roboto",sans-serif}
.field.msg{height:87px;margin-bottom:9px}
.quote-btn{background:var(--red);color:var(--white);text-align:center;font-size:11px;height:22px;line-height:20px;border:1px solid #fff;font-family:"Montserrat",sans-serif}

/* tagline band */
.tagline{left:0;top:542px;width:820px;height:78px;background:var(--band);color:var(--white);font-family:"Roboto",sans-serif;font-weight:300;font-size:16.5px;text-align:center;line-height:21px;padding-top:19px;letter-spacing:.2px}

/* services */
.section-title{left:0;top:662px;width:820px;text-align:center;font-family:"Roboto",sans-serif;font-weight:400;font-size:20px;color:#777}
.rule{top:676px;height:1px;background:#cfcfcf}
.service{width:200px}
.service .icon{position:absolute;left:-36px;top:0}
.service h3{font-family:"Roboto",sans-serif;font-weight:400;font-size:12px;color:#444;letter-spacing:1px}
.service p{font-size:8.6px;color:var(--muted);line-height:11.5px;margin-top:4px}
.service a{font-size:8.6px;color:var(--red);text-decoration:none}

/* contact */
.contact{left:333px;top:964px;font-family:"Roboto",sans-serif;font-size:13px;color:#888;line-height:16px}
.contact-icon{left:295px;top:967px}

/* footer */
.footer{left:0;top:1021px;width:820px;height:73px;background:var(--red);color:var(--white);font-size:10px;font-family:"Montserrat",sans-serif}
.footer .links span{position:absolute;top:21px}
.footer .social{left:368px;top:49px;gap:22px}
</style>
</head>
<body>
<div class="page">

  <header class="abs topbar">
    <div class="abs call">Call Today : 812-555-0147</div>
    <div class="abs social"><span></span><span></span><span></span></div>
    <div class="abs search">Search
      <svg width="17" height="17" viewBox="0 0 17 17"><circle cx="10" cy="7" r="5.5" fill="none" stroke="#fff" stroke-width="1.8"/><line x1="6" y1="11" x2="1.5" y2="15.5" stroke="#fff" stroke-width="2"/></svg>
    </div>
  </header>

  <div class="abs brand">
    <div class="brand-name"><i></i>Bright Lane Fixers</div>
    <div class="brand-sub">And Maintenance</div>
  </div>

  <nav>
    <span class="abs nav active" style="left:156px">HOME</span>
    <span class="abs nav" style="left:250px">ABOUT</span>
    <span class="abs nav" style="left:353px">SERVICES</span>
    <span class="abs nav" style="left:484px">BLOG</span>
    <span class="abs nav" style="left:567px">CONTACT</span>
  </nav>

  <section class="abs hero" role="img" aria-label="Photo of a brick two-storey house with a shingled roof and trees">
    <form class="abs quote-form">
      <div class="field">Name :</div>
      <div class="field">Email :</div>
      <div class="field">Phone :</div>
      <div class="field msg">Your message :</div>
      <div class="quote-btn">GET QUOTE</div>
    </form>
    <div class="abs hero-overlay">
      <p>Looking for someone to help get your listing ready to show?</p>
      <p>A complete Home Repair Solution? Did an inspection reveal repairs needed before closing?</p>
      <h1>BRIGHT LANE FIXERS CAN HELP!</h1>
    </div>
  </section>

  <div class="abs tagline">One Name, One number, One call means one service for fast timely quotes,<br>home repairs and updates for you and/or your clients.</div>

  <div class="abs rule" style="left:0;width:294px"></div>
  <div class="abs rule" style="left:526px;width:294px"></div>
  <h2 class="abs section-title">Home Repair Services</h2>

  <article class="abs service" style="left:75px;top:729px">
    <svg class="icon" width="26" height="26" viewBox="0 0 26 26"><path d="M3 23 L20 6 M6 4 L23 21" stroke="#666" stroke-width="3"/></svg>
    <h3>CARPENTRY</h3>
    <p>Stairs, Floors, Decks, Fences Storage sheds, Storage shelving and doorsVapor barrier repair/installation, Attic and crawl space</p>
    <a>Read more →</a>
  </article>
  <article class="abs service" style="left:318px;top:729px;width:210px">
    <svg class="icon" width="26" height="26" viewBox="0 0 26 26"><rect x="3" y="4" width="20" height="18" fill="none" stroke="#666" stroke-width="2"/><line x1="13" y1="4" x2="13" y2="22" stroke="#666" stroke-width="2"/></svg>
    <h3>Doors &amp; Windows</h3>
    <p>Weatherstripping, Replacements Glass and Screen Installation and Repair, Install lockets</p>
    <a>Read more →</a>
  </article>
  <article class="abs service" style="left:566px;top:729px;width:200px">
    <svg class="icon" width="26" height="26" viewBox="0 0 26 26"><circle cx="10" cy="6" r="3" fill="#666"/><path d="M8 10 L14 12 L18 22 M9 11 L5 22" stroke="#666" stroke-width="3" fill="none"/></svg>
    <h3>SMALL CONSTRUCTION</h3>
    <p>Stairs, Floors, Decks, Fences Storage sheds, Storage shelves Masonry</p>
    <a>Read more →</a>
  </article>
  <article class="abs service" style="left:76px;top:820px">
    <svg class="icon" width="28" height="24" viewBox="0 0 28 24"><path d="M2 8 H14 V18 H22" stroke="#666" stroke-width="4" fill="none"/><rect x="20" y="14" width="6" height="8" fill="#666"/></svg>
    <h3>PLUMBING</h3>
    <p>Bathrooms, Kitchens, Washer/Dryer Hook Up Clogged drains, Toilets, Tubs/Showers Sinks, Garbage disposals, Leaking faucets vent repair</p>
    <a>Read more →</a>
  </article>
  <article class="abs service" style="left:318px;top:820px;width:210px">
    <svg class="icon" width="26" height="20" viewBox="0 0 26 20"><path d="M2 14 L10 4 L24 10" stroke="#666" stroke-width="2" fill="none"/><line x1="4" y1="8" x2="4" y2="16" stroke="#666" stroke-width="2"/></svg>
    <h3>ROOFING MAINTENANCE</h3>
    <p>Painting, Pressure/Power washing Heavy lifting, Property Clean Outs Minor Repairs Vinyl Siding, Gutters, Clean and seal tile, Caulking, Patch and repair drywall, replace hard to reach light bulbs, Painting, Cosmetic repair, Debris removal.</p>
    <a>Read more →</a>
  </article>
  <article class="abs service" style="left:561px;top:820px;width:170px">
    <svg class="icon" style="left:-30px" width="20" height="28" viewBox="0 0 20 28"><path d="M6 2 V8 M14 2 V8 M3 8 H17 V15 L10 20 L3 15 Z M10 20 V27" stroke="#666" stroke-width="2" fill="none"/></svg>
    <h3>ELECTRICAL</h3>
    <p>Bright Lane Fixers has licensed electricians who can rewire your entire house, or just a GFCI. We can respond to your electrical needs quickly. Code/Service Upgrades Fuses and Circuit Breakers Recessed Lighting Ceiling Fixtures You Name It!</p>
    <a>Read more →</a>
  </article>

  <svg class="abs contact-icon" width="24" height="30" viewBox="0 0 24 30"><path d="M5 2 C1 4 1 12 6 20 C11 28 16 29 20 27 L17 21 L13 22 C10 18 8 13 9 9 L12 7 Z" fill="#999"/></svg>
  <div class="abs contact">812-555-0147<br>Sam@brightlanefixers.com</div>

  <footer class="abs footer">
    <div class="links">
      <span style="left:291px">Home</span>
      <span style="left:358px">About</span>
      <span style="left:425px">Services</span>
      <span style="left:492px">Contact</span>
    </div>
    <div class="abs social"><span></span><span></span><span></span></div>
  </footer>

</div>
</body>
</html>
```